Broschüre im Bereich Steuerberatung
Zielgruppe
Steuerberatung
Aufgabenstellung
Die Seite 1 wäre eigentlich fertig, natürlich bin ich offen für Optimierungen. Die weiteren fünf Seiten gilt es noch zu gestalten:
Seite 1
Buchhaltung
Lohnwesen
Steuern
Firmengründung
Kontakt

```html
<!DOCTYPE html>
<html lang="de">
<head>
<meta charset="utf-8">
<title>Broschüre Treuhand – Seitenübersicht</title>
<link href="https://fonts.googleapis.com/css2?family=Jost:wght@400;500;700&family=Oswald:wght@400&family=Source+Serif+4:ital,wght@0,300;0,400;1,400&display=swap" rel="stylesheet">
<style>
:root{
  --navy:#1d3f7a;
  --orange:#e8581c;
  --green:#9db43d;
  --stage:#dcdbd3;
  --paper:#ffffff;
  --ink:#2a2f3a;
}
*{box-sizing:border-box;margin:0;padding:0}
html,body{width:878px;height:1200px;overflow:hidden;background:var(--stage)}
body{position:relative;font-family:'Jost',sans-serif;color:var(--ink)}
.page{position:absolute;width:369px;height:261px;background:var(--paper);overflow:hidden}
.tagline{position:absolute;left:16px;top:31px;font-family:'Oswald',sans-serif;font-size:9.5px;letter-spacing:2.6px;color:var(--navy);white-space:nowrap;display:flex;align-items:center}
.tagline .dot{display:inline-block;width:4px;height:4px;border-radius:50%;background:var(--orange);margin:0 4px 0 1px}
.photo{position:absolute;left:16px;top:52px;width:176px;height:176px}
.photo.city{background:linear-gradient(160deg,#8a6c9a 0%,#7e7ea8 30%,#6c7e72 60%,#8b7a55 100%)}
.photo.trees{background:linear-gradient(160deg,#c98a6a 0%,#9a8a7a 25%,#6f8a4a 55%,#a08a3c 100%)}
.photo.glass{background:linear-gradient(160deg,#5a6f9a 0%,#6c8aa0 35%,#5d8a4a 65%,#8e8a40 100%)}
.photo.street{background:linear-gradient(160deg,#b08a78 0%,#8c8a78 30%,#5f7c48 60%,#7c7468 100%)}
.photo.canal{background:linear-gradient(160deg,#b48a9a 0%,#a0869a 30%,#6f7a4c 60%,#5a4c5c 100%)}
.hero{position:absolute;right:6px;font-family:'Source Serif 4',serif;font-weight:300;color:#fff;text-align:right;line-height:.82}
.url{position:absolute;left:103px;top:163px;font-size:6px;font-weight:500;color:var(--orange)}
.col{position:absolute;left:200px;width:154px}
.h-lead{font-size:5.6px;font-weight:700;color:var(--navy);line-height:1.35}
.h-sub{font-size:4.4px;font-weight:700;color:var(--orange);line-height:1.4;margin-top:3px}
.body{font-size:3.6px;line-height:1.5;color:var(--ink);text-align:justify}
.body p+p{margin-top:4px}
.sec{position:absolute;width:72px}
.sec h3{font-size:5.4px;font-weight:700;color:var(--navy);letter-spacing:.2px;margin-bottom:2px}
.portrait{position:absolute;left:285px;top:71px;width:74px;height:52px;background:linear-gradient(135deg,#d8d8d6,#b9b0a8)}
.calc-badge{position:absolute;width:46px;height:46px;border-radius:50%;background:var(--green)}
.calc-badge svg{position:absolute;left:11px;top:11px}
.promo{position:absolute;font-size:4.2px;font-weight:700;color:var(--orange);line-height:1.45}
.bullet{display:flex;gap:4px;margin-bottom:5px}
.bullet .arrow{flex:0 0 8px;height:8px;border-radius:50%;background:var(--orange);position:relative}
.bullet p{font-size:3.7px;font-weight:700;color:var(--navy);line-height:1.45;text-align:justify}
.step{position:absolute;left:322px;width:38px;text-align:center}
.step svg{display:block;margin:0 auto}
.step span{display:block;font-size:3.6px;font-weight:700;color:var(--navy);line-height:1.3;margin-top:1px}
.sub-head{font-size:5.6px;font-weight:700;color:var(--navy);letter-spacing:.4px;margin:5px 0 2px}
.serif-claim{font-family:'Source Serif 4',serif;font-size:6px;color:var(--navy);line-height:1.3}
.serif-claim b{font-family:'Jost',sans-serif;font-weight:700;font-size:5.6px}
.serif-claim i{font-style:italic}
.price-card{position:absolute;left:200px;top:144px;width:53px;height:82px;background:#fff;border-radius:3px;box-shadow:0 1px 5px rgba(0,0,0,.18);padding:5px 4px}
.price-card h4{font-size:3.8px;font-weight:700;color:var(--navy);text-align:center;line-height:1.35}
.price-card .price{font-size:3.8px;font-weight:700;color:var(--orange);text-align:center;margin-bottom:4px}
.price-card li{list-style:none;font-size:2.3px;line-height:1.35;color:var(--ink);margin-bottom:2px;padding-left:4px;position:relative}
.price-card li::before{content:"✓";position:absolute;left:0;color:var(--orange);font-size:2.6px}
.price-card .note{font-size:2.2px;color:#999;margin-top:3px;border-top:.4px solid #ddd;padding-top:2px}
.price-card .cta{display:block;margin:3px auto 0;width:36px;height:8px;border-radius:4px;background:var(--green);color:#fff;font-size:2.4px;text-align:center;line-height:8px}
.brand{font-family:'Source Serif 4',serif;font-weight:400;font-size:17px;color:var(--navy);display:flex;align-items:center;gap:3px}
.brand .mark{width:6px;height:6px;border-radius:50%;background:var(--orange)}
.address{font-size:4px;line-height:1.55;color:var(--ink)}
.address .acc{color:var(--orange)}
.map{position:absolute;background:linear-gradient(135deg,#f3f4f8,#e6e9f1)}
.divider{position:absolute;left:184px;top:118px;width:.6px;height:107px;background:var(--navy);opacity:.5}
</style>
</head>
<body>

<!-- Seite 1: Übersicht -->
<section class="page" style="left:47px;top:46px">
  <div class="tagline">STEUERN<i class="dot"></i>MEHRWERT<i class="dot"></i>TREUHAND<i class="dot"></i></div>
  <div class="photo city" role="img" aria-label="Foto einer Stadtstrasse mit Bürogebäuden und Bäumen">
    <div class="hero" style="top:14px;font-size:34px">berger</div>
    <div class="url">bergertreuhand.ch</div>
  </div>
  <div class="col" style="top:52px">
    <div class="h-lead">Zuverlässig und partnerschaftlich:<br>Ihre massgeschneiderten Treuhand-Lösungen</div>
    <div class="body" style="width:78px;margin-top:5px">
      <p>Sie möchten Ihre Steuern, Ihre Buchhaltung oder Ihr Lohnwesen in verlässliche Hände geben? Sie legen Wert auf eine persönliche Betreuung mit gleichbleibendem Ansprechpartner, auf individuelle Strategien und auf ein angenehmes Miteinander?</p>
      <p>Dann freue ich mich auf Ihre Kontaktaufnahme.</p>
    </div>
  </div>
  <div class="portrait" role="img" aria-label="Porträtfoto der Beraterin"></div>
  <div class="sec" style="left:200px;top:140px">
    <h3>BUCHHALTUNG</h3>
    <div class="body">Buchhaltung ist komplex und aufwendig – das kostet Unternehmer viel Zeit, die sie anderswo wertschöpfend einsetzen könnten. Mithilfe moderner Hilfsmittel und bewährter Prozesse entlaste ich Sie zuverlässig und zum Fixpreis.</div>
  </div>
  <div class="sec" style="left:283px;top:140px">
    <h3>STEUERERKLÄRUNG</h3>
    <div class="body">Jeder möchte seine Steuerlast optimieren, nur wenige setzen sich aktiv damit auseinander. Denn das kostet Zeit und verlangt nach umfangreichem Wissen. Vertrauen Sie mir Ihre Steuererklärungen an – und holen Sie sich zurück, was Ihnen zusteht.</div>
  </div>
  <div class="sec" style="left:200px;top:190px">
    <h3>LOHNWESEN</h3>
    <div class="body">Entscheiden Sie selbst, in welcher Form Sie auf meine Expertise zugreifen, um sich beim Thema Lohnbuchhaltung zu entlasten.</div>
  </div>
  <div class="sec" style="left:283px;top:190px">
    <h3>FIRMENGRÜNDUNG</h3>
    <div class="body">Gründen Sie Ihre Schweizer Gesellschaft schnell und sicher. Mit meiner langjährigen Erfahrung, meinem Wissen und meiner Zusammenarbeit mit einem versierten Notar unterstütze ich Sie zuverlässig – auch über Ihre Gründung hinaus.</div>
  </div>
</section>

<!-- Seite 2: Buchhaltung -->
<section class="page" style="left:452px;top:46px">
  <div class="tagline">ADDITION<i class="dot"></i>SUBTRAKTION<i class="dot"></i>ERFOLG<i class="dot"></i></div>
  <div class="photo trees" role="img" aria-label="Foto von Bäumen vor Hochhäusern im Abendlicht">
    <div class="hero" style="top:12px;font-size:36px">buch-<br>haltung</div>
  </div>
  <div class="calc-badge" style="left:168px;top:187px">
    <svg width="24" height="24" viewBox="0 0 24 24" fill="none" stroke="#fff" stroke-width="1.6"><rect x="1" y="1" width="22" height="22" rx="2"/><path d="M4 7h5M15 5l4 4M19 5l-4 4M4 17h5M6.5 14.5v5M15 16h4M15 19h4"/></svg>
  </div>
  <div class="promo" style="left:223px;top:206px">Mit individuellem Preisrechner auf:<br>www.bergertreuhand.ch/treuhand/buchhaltung</div>
  <div class="col" style="top:52px">
    <div class="h-lead">Buchhaltung kostet Sie viel Zeit<br>– Ich gebe Sie Ihnen zurück</div>
    <div class="h-sub">Ich übernehme Ihre Buchhaltung –<br>akribisch, verlässlich, verantwortungsvoll</div>
  </div>
  <div class="body" style="position:absolute;left:200px;top:90px;width:70px">
    <p>Unternehmer zählen die Buchhaltung in der Regel nicht zu ihren Leidenschaften.</p>
    <p>Und dennoch ist eine ordentliche Buchhaltung das Rückgrat eines jeden erfolgreichen Betriebs. Es ergibt also durchaus Sinn, hierfür ausreichend Ressourcen bereit zu stellen – jedoch nicht die eigenen.</p>
    <p>Wenn Sie selbst oder Ihre Mitarbeiter sich um dieses komplexe „Pflichtthema“ kümmern, bleiben andere, wertschöpfende Tätigkeiten auf der Strecke: neue Kunden akquirieren, Produkte weiterentwickeln, Services ausbauen usw.</p>
  </div>
  <div class="body" style="position:absolute;left:283px;top:90px;width:70px">
    <p>Die Folge: Es kommt zu unnötigem Mehraufwand und die Entwicklung Ihres Unternehmens schreitet langsamer voran als geplant.</p>
    <p>Beides ist unschön – und beides lässt sich leicht vermeiden. Nutzen Sie Ihre wertvolle Zeit lieber gewinnbringend und überlassen Sie Ihre Buchhaltung einem Profi.</p>
    <p>Mit viel Erfahrung, Wissen und Leidenschaft kümmere ich mich um Ihre Geschäftsvorfälle, während Ihr Team und Sie sich auf Ihre Kerntätigkeit fokussieren.</p>
  </div>
</section>

<!-- Seite 3: Lohnwesen -->
<section class="page" style="left:47px;top:330px">
  <div class="tagline">IHRE ZUKUNFT<i class="dot"></i>MEHR<i class="dot"></i>LOHN<i class="dot"></i></div>
  <div class="photo glass" role="img" aria-label="Foto einer Glasfassade mit grünem Baum davor">
    <div class="hero" style="top:12px;font-size:36px">lohn-<br>wesen</div>
  </div>
  <div class="col" style="top:52px">
    <div class="h-lead">Lohnbuchhaltung ohne Stress:<br>So gewinnen Sie mehr Zeit</div>
    <div class="h-sub">Ich erledige Ihr Lohnwesen – präzise, sicher, zuverlässig</div>
  </div>
  <div class="body" style="position:absolute;left:200px;top:87px;width:70px">
    <p>Sicherlich stimmen Sie mir zu, wenn ich das Personalwesen und die Saläradministration zu den sensiblen Bereichen Ihres Unternehmens zähle. Schliesslich erwarten Ihre Mitarbeiter, dass ihre Gehälter pünktlich auf dem Konto eingehen.</p>
    <p>Doch die Lohnbuchhaltung ist komplex und daher zeitaufwendig – sie bindet wertvolle Ressourcen, die Ihnen für andere, wertschöpfende Tätigkeiten fehlen.</p>
    <p>Holen Sie sich die Zeit zurück und legen Sie Ihre Lohnbuchhaltung in meine Hände. Dabei haben Sie die Wahl zwischen Optimierung und Outsourcing.</p>
  </div>
  <div style="position:absolute;left:277px;top:85px;width:78px">
    <div class="bullet"><i class="arrow"><svg width="8" height="8" viewBox="0 0 8 8" fill="none" stroke="#fff" stroke-width=".9"><path d="M2 4h4M4.4 2.4 6 4 4.4 5.6"/></svg></i><p>Sie übernehmen die vorbereitenden Arbeiten, während ich mich um die Umsetzung kümmere. So optimieren wir gemeinsam Ihre Vorgänge und entlasten Ihre interne Buchhaltung.</p></div>
    <div class="bullet"><i class="arrow"><svg width="8" height="8" viewBox="0 0 8 8" fill="none" stroke="#fff" stroke-width=".9"><path d="M2 4h4M4.4 2.4 6 4 4.4 5.6"/></svg></i><p>Sie lagern Ihre Lohnbuchhaltung an mich aus. Insbesondere kleine und mittlere Unternehmen profitieren vom Outsourcing immens, da sie sich von diesem Thema komplett befreien.</p></div>
  </div>
</section>

<!-- Seite 4: Steuern -->
<section class="page" style="left:452px;top:330px">
  <div class="tagline">ERFOLG LÄSST SICH STEUERN<i class="dot" style="margin-left:4px"></i></div>
  <div class="photo street" role="img" aria-label="Foto einer baumgesäumten Stadtstrasse">
    <div class="hero" style="top:12px;font-size:36px">steuern</div>
  </div>
  <div class="calc-badge" style="left:168px;top:173px">
    <svg width="24" height="24" viewBox="0 0 24 24" fill="none" stroke="#fff" stroke-width="1.6"><rect x="1" y="1" width="22" height="22" rx="2"/><path d="M4 7h5M15 5l4 4M19 5l-4 4M4 17h5M6.5 14.5v5M15 16h4M15 19h4"/></svg>
  </div>
  <div class="promo" style="left:221px;top:190px">Mit individuellem Preisrechner auf:<br>www.bergertreuhand.ch/steuererklaerung</div>
  <div class="col" style="top:52px;width:115px">
    <div class="h-lead">Professionell und transparent:<br>Ihre Steuererklärung und Steuerberatung</div>
    <div class="h-sub">Ich kümmere mich persönlich um Ihre Steuerangelegenheiten</div>
    <div class="body" style="margin-top:7px;width:100px">Steuern sind ein sensibles Thema – schliesslich geht es um Ihr Geld. Setzen Sie gleich auf professionelle Unterstützung: Vermeiden Sie teure Fehler, sparen Sie viel Zeit und schonen Sie Ihre Nerven.</div>
    <div class="sub-head">FÜR PRIVATPERSONEN</div>
    <div class="body" style="width:100px">
      <p>Weshalb ich mir viel Zeit für Sie nehme und Sie individuell betreue? Weil wir mit Konzepten „von der Stange“ bei Ihrer Steuererklärung nicht weit kommen.</p>
      <p>Hingegen habe ich die Abläufe rund um Ihre Steuerberatung standardisiert – um es Ihnen einfach zu machen: Wir tauschen uns per E-Mail, Telefon, Videocall oder per Post aus. So erhalten Sie schnelle Ergebnisse und sparen sich Weg und Kosten für einen persönlichen Termin.</p>
    </div>
  </div>
  <div class="step" style="top:83px"><svg width="16" height="14" viewBox="0 0 16 14" fill="none" stroke="var(--navy)" stroke-width=".8"><rect x="3" y="1" width="9" height="12" rx="1"/><path d="M5 4h5M5 6.5h5M5 9h3M10 11l4-6"/></svg><span>Checkliste<br>ausfüllen</span></div>
  <div class="step" style="top:116px"><svg width="16" height="14" viewBox="0 0 16 14" fill="none" stroke="var(--orange)" stroke-width=".8"><rect x="4" y="1" width="9" height="9" rx="1"/><path d="M6 4h5M6 6.5h5M2 10c2 0 3 2 6 2h6"/></svg><span>Unterlagen<br>bereitstellen</span></div>
  <div class="step" style="top:148px"><svg width="16" height="12" viewBox="0 0 16 12" fill="none" stroke="var(--orange)" stroke-width=".8"><rect x="2" y="2" width="12" height="8" rx="1"/><path d="M2 2l6 5 6-5"/></svg><span>Unterlagen<br>übergeben</span></div>
  <div class="step" style="top:180px"><svg width="16" height="14" viewBox="0 0 16 14" fill="none" stroke="var(--navy)" stroke-width=".8"><rect x="3" y="1" width="10" height="12" rx="1"/><path d="M5 8h6M5 10.5h6"/><text x="8" y="5.5" font-size="3.6" text-anchor="middle" fill="var(--navy)" stroke="none" font-family="Jost,sans-serif" font-weight="700">TAX</text></svg><span>Meine<br>Arbeit</span></div>
  <div class="step" style="top:214px"><svg width="16" height="14" viewBox="0 0 16 14" fill="none" stroke="var(--orange)" stroke-width=".8"><path d="M4 1h6l3 3v9H4z"/><path d="M8.5 11V5M6.5 7l2-2 2 2"/></svg><span>Unterschreiben<br>+ Abgeben</span></div>
</section>

<!-- Seite 5: Firmengründung -->
<section class="page" style="left:47px;top:615px">
  <div class="tagline">DON'T DREAM IT.<i class="dot"></i>DO IT!<i class="dot" style="margin-left:4px"></i></div>
  <div class="photo canal" role="img" aria-label="Foto von Fahrrädern an einem Kanal in der Abenddämmerung">
    <div class="hero" style="top:12px;font-size:33px">firmen-<br>gründung</div>
  </div>
  <div class="col" style="top:52px">
    <div class="h-lead">Berger Treuhand:<br>Professionelle Unternehmensgründung mit System</div>
    <div class="h-sub">Berger Treuhand - Ihr kompetenter Partner</div>
  </div>
  <div class="body" style="position:absolute;left:200px;top:84px;width:70px">Die Unternehmensgründung gehört zu den emotionalsten Erlebnissen in der Karriere. Gut, wenn man hierbei einen verlässlichen Partner hat, der einen kühlen Kopf bewahrt und sich bis ins Detail mit sämtlichen Anforderungen auskennt.</div>
  <div class="body" style="position:absolute;left:283px;top:84px;width:72px">Schon seit mehr als 13 Jahren unterstütze ich Start-ups auf ihrem Weg an die Spitze – vom ersten Tag an rund um die Gründung und danach bei der Buchhaltung, im Lohnwesen und bei den Steuern.</div>
  <div class="serif-claim" style="position:absolute;left:200px;top:125px;width:120px"><b>Kompetenter Service.</b> <i>Komplett ohne persönlichen Notartermin.</i></div>
  <div class="price-card">
    <h4>FULLSERVICE-PAKET<br>GRÜNDUNG</h4>
    <div class="price">CHF 750.-</div>
    <ul>
      <li>Telefonische Beratung</li>
      <li>Erstellen der Gründungsdokumente</li>
      <li>Vertretung beim Notar durch Vollmacht</li>
      <li>Anmeldung beim Handelsregisteramt</li>
    </ul>
    <div class="note">zzgl. HR-Gebühren</div>
    <span class="cta">JETZT GRÜNDEN ›</span>
  </div>
</section>

<!-- Seite 6: Kontakt -->
<section class="page" style="left:452px;top:615px">
  <div class="col" style="left:16px;top:53px;width:300px">
    <div class="h-lead">Zuverlässig und partnerschaftlich:<br>Ihre massgeschneiderten Treuhand-Lösungen</div>
    <div class="h-sub">Sie haben noch Fragen? Rufen Sie uns an oder senden<br>Sie uns eine Mail, wir helfen Ihnen gerne weiter.</div>
  </div>
  <div class="brand" style="position:absolute;left:16px;top:128px"><span>berger</span><i class="mark"></i></div>
  <div class="address" style="position:absolute;left:16px;top:166px">
    <div class="acc">Berger Treuhand Consulting GmbH</div>
    <div class="acc">Lindenweg 14</div>
    <div class="acc">6004 Luzern</div>
    <div>+41 (0)41 555 01 20</div>
    <div>+41 (0)79 555 01 21 Mobile</div>
    <div>info@bergertreuhand.ch</div>
  </div>
  <div class="map" style="left:79px;top:120px;width:96px;height:109px" role="img" aria-label="Lageplan des Standorts Luzern"></div>
  <div class="divider"></div>
  <div class="brand" style="position:absolute;left:197px;top:128px"><span>berger</span><i class="mark"></i></div>
  <div class="address" style="position:absolute;left:197px;top:166px">
    <div class="acc">Berger Treuhand Consulting GmbH</div>
    <div class="acc">Ahornweg 8</div>
    <div class="acc">8810 Horgen</div>
    <div>+41 (0)41 555 01 20</div>
    <div>+41 (0)79 555 01 21 Mobile</div>
    <div>info@bergertreuhand.ch</div>
  </div>
  <div class="map" style="left:262px;top:120px;width:93px;height:109px" role="img" aria-label="Lageplan des Standorts Horgen"></div>
</section>

<!-- Seite 7: Kontakt, Variante -->
<section class="page" style="left:47px;top:897px">
  <div class="col" style="left:16px;top:16px;width:300px">
    <div class="h-lead">Zuverlässig und partnerschaftlich:<br>Ihre massgeschneiderten Treuhand-Lösungen</div>
    <div class="h-sub">Sie haben noch Fragen? Rufen Sie uns an oder senden<br>Sie uns eine Mail, wir helfen Ihnen gerne weiter.</div>
  </div>
  <div class="brand" style="position:absolute;left:16px;top:72px"><span>berger</span><i class="mark"></i></div>
  <div class="address" style="position:absolute;left:16px;top:111px">
    <div>Berger Treuhand Consulting GmbH</div>
    <div>Lindenweg 14</div>
    <div>6004 Luzern</div>
    <div>+41 (0)41 555 01 20</div>
    <div>+41 (0)79 555 01 21 Mobile</div>
    <div>info@bergertreuhand.ch</div>
  </div>
  <div class="brand" style="position:absolute;left:200px;top:72px"><span>berger</span><i class="mark"></i></div>
  <div class="address" style="position:absolute;left:200px;top:111px">
    <div>Berger Treuhand Consulting GmbH</div>
    <div>Ahornweg 8</div>
    <div>8810 Horgen</div>
    <div>+41 (0)41 555 01 20</div>
    <div>+41 (0)79 555 01 21 Mobile</div>
    <div>info@bergertreuhand.ch</div>
  </div>
  <div class="map" style="left:16px;top:151px;width:139px;height:96px" role="img" aria-label="Lageplan des Standorts Luzern"></div>
  <div class="map" style="left:200px;top:151px;width:138px;height:96px" role="img" aria-label="Lageplan des Standorts Horgen"></div>
</section>

</body>
</html>
```